Web Design Project

We are looking for a web page (home) page design for a website that offers Virtual Internet Marketing services.

The Company is called Brindle Marketing, the services we provide are as follows:

Web Design
Social Media Management
SEO/PPC Traffic
Display
Mobile Apps
On & Offline Marketing Services

We see so many web marketing companies that struggle to produce their own great designs and call to actions. 99% of web companies do not understand marketing, so how can they help their customers drive traffic and produce sales!

We require a design that is professional yet fresh and funky! Our goal with the home page is to help prospects understand that our core business is to help them succeed and make more money, by utilising our on and offline marketing experience. We also offer done for you solutions which include - websites, design, traffic, email campaigns etc.

Included should be obvious call to actions to view our services and get our free guide/video

- A clear value proposition that identifies target audience (those that are struggling to make the web work for them)

- Easy to use navigation

We need to include an optin form where we exchange a free training guide or video series in return for an email address, above the fold to the right of the page!

We like the following to provide you with ideas:

http://www.plankorbit.com/
http://www.morvane.co.uk/
http://www.gristlepond.com/
http://www.tarnby.co.uk/ (quite like but too jumbled - too much going on)

Colours are optional, however fresh, vibrant and professional looking.

The final design should be easy on the eye, not lead to any confusion as to what we do and be simple to navigate.

Industry/Entity Type

Marketing

Requirements
Must have
• Optin form
Footer section
showcase of services offered.

```html
<!DOCTYPE html>
<html lang="en">
<head>
<meta charset="utf-8">
<title>Brindle Marketing</title>
<link href="https://fonts.googleapis.com/css2?family=PT+Sans:wght@400;700&family=Oswald:wght@500&family=Arimo:wght@400&display=swap" rel="stylesheet">
<style>
:root{
  --dark:#1c1c1c;
  --blue:#1f9fe0;
  --blue-deep:#0d86c9;
  --blue-title:#1d77b6;
  --paper:#f4f4f2;
  --card:#f7f7f7;
  --ink:#333;
  --muted:#555;
  --line:#d6d6d6;
}
*{margin:0;padding:0;box-sizing:border-box}
html,body{width:847px;height:1200px;overflow:hidden}
body{position:relative;background:var(--paper);font-family:"PT Sans",sans-serif;color:var(--ink)}
.abs{position:absolute}
.header{left:0;top:0;width:847px;height:57px;background:linear-gradient(#2a2a2a,#0e0e0e)}
.brand{left:78px;top:0;width:138px;height:66px;background:#fff;box-shadow:0 3px 6px rgba(0,0,0,.35);display:flex;align-items:center;justify-content:center;text-align:center;font:700 19px/1.05 "PT Sans",sans-serif;color:var(--blue-title)}
.nav{left:391px;top:0;height:57px;display:flex}
.nav a{display:flex;flex-direction:column;align-items:center;justify-content:flex-end;padding-bottom:8px;height:57px;color:#fff;text-decoration:none;font-size:10.5px;border-left:1px solid #333}
.nav a svg{margin-bottom:6px}
.nav .active{background:linear-gradient(#35b3f0,var(--blue-deep))}
.hero{left:0;top:57px;width:847px;height:284px;background:linear-gradient(#4fc3f6,var(--blue) 60%,var(--blue-deep))}
.follow{left:589px;top:77px;color:#fff;font-size:13px;display:flex;align-items:center;gap:6px}
.follow i{display:block;width:15px;height:15px;border-radius:50%;background:#fff;opacity:.85}
.hero-title{left:80px;top:106px;font:500 22px "Oswald",sans-serif;color:#fff}
.hero-sub{left:80px;top:138px;width:240px;font-size:14px;line-height:15.5px;color:#fff}
.hero-text{left:83px;top:193px;width:236px;font:8.8px/15.5px "Arimo",sans-serif;color:#fff;text-align:justify}
.learn{left:81px;top:281px;width:120px;height:26px;border-radius:13px;background:linear-gradient(#6a6a6a,#2d2d2d);border:1px solid #999;color:#fff;font:500 13px/24px "Oswald",sans-serif;padding-left:12px}
.btn-arrow{position:absolute;right:6px;top:4px;width:17px;height:17px;border-radius:50%;background:#eee}
.btn-arrow:after{content:"";position:absolute;left:7px;top:5px;border-left:5px solid #333;border-top:3.5px solid transparent;border-bottom:3.5px solid transparent}
.slider{left:346px;top:106px;width:415px;height:235px;background:#fff;box-shadow:0 6px 8px rgba(0,0,0,.2)}
.slide{position:absolute;left:6px;top:6px;width:402px;height:224px;background:radial-gradient(circle at 55% 45%,#fafafa,#9a9a9a)}
.arrow{top:210px;width:24px;height:24px;border-radius:50%;background:#fff;box-shadow:0 1px 3px rgba(0,0,0,.4)}
.arrow:after{content:"";position:absolute;top:7px;border-top:5px solid transparent;border-bottom:5px solid transparent}
.arrow.prev{left:333px}.arrow.prev:after{left:7px;border-right:7px solid #444}
.arrow.next{left:755px}.arrow.next:after{left:10px;border-left:7px solid #444}
.optin-bar{left:109px;top:366px;width:624px;height:38px;background:#eee;border:1px solid #ddd;border-radius:3px}
.optin-title{left:128px;top:375px;font:700 16px "PT Sans",sans-serif;color:var(--blue-title)}
.field{background:#fff;border:1px solid #ccc;border-radius:12px;font:8.5px/22px "PT Sans",sans-serif;color:#333;padding-left:10px}
.dark-btn{border-radius:11px;background:linear-gradient(#666,#2a2a2a);color:#fff;font:500 10px/20px "Oswald",sans-serif;padding-left:10px}
.blue-btn{border-radius:9px;background:linear-gradient(#3ab4f2,#0f7fc6);border:1px solid #0b6aa6;color:#fff;font-size:8.5px;text-align:center;line-height:16px}
h2.section{left:75px;top:440px;font:700 17px "PT Sans",sans-serif;color:#222}
.rule{left:70px;top:468px;width:486px;border-top:1px dotted #aaa}
.feature-img{left:84px;top:482px;width:176px;height:122px;border-radius:4px;background:linear-gradient(#e8eef3,#cfd9e2)}
.about-text{left:274px;top:478px;width:287px;font-size:8.3px;line-height:12.8px;text-align:justify;color:#333}
.about-text p+p{margin-top:12px}
.side{left:584px;top:438px;width:190px;height:172px;background:#fff;border:1px solid #e4e4e4}
.side h3{position:absolute;left:9px;top:8px;font:700 15.5px "PT Sans",sans-serif;color:#222}
.side p{position:absolute;left:11px;top:36px;width:172px;font-size:8px;line-height:12.5px;color:#333}
.card{width:219px;height:112px;background:linear-gradient(#fff,#f0f0f0);border:1px solid #e2e2e2;border-radius:4px;box-shadow:0 6px 6px -4px rgba(0,0,0,.15)}
.card h4{position:absolute;left:16px;top:8px;font:700 14px "PT Sans",sans-serif;color:#333}
.card .icon{position:absolute;left:14px;top:34px;width:64px;height:64px;border-radius:10px;border:1px solid #d0d0d0;box-shadow:0 2px 4px rgba(0,0,0,.25)}
.card p{position:absolute;left:94px;top:38px;width:116px;font:8.6px/12.7px "Arimo",sans-serif;color:#555}
.partners{left:80px;top:948px;width:690px;display:flex;justify-content:space-between;align-items:center;font-size:12px;color:#777}
.partners span:nth-child(5){background:#555;color:#fff;padding:1px 6px;font-size:9px}
.foot-rule{left:72px;top:1002px;width:702px;border-top:1px solid #ccc}
.col-title{font-size:15px;color:#333}
.vsep{top:1015px;height:140px;border-left:1px solid #ddd}
.flink{font-size:8.6px;line-height:17px;color:#333;list-style:none}
.flink li:before{content:"";display:inline-block;margin-right:6px;border-left:3px solid #333;border-top:2.5px solid transparent;border-bottom:2.5px solid transparent;vertical-align:1px}
.social{font:700 13px "PT Sans",sans-serif;color:#1d5fa8;display:flex;align-items:center;gap:8px}
.social i{display:block;width:20px;height:20px;background:#3b6eb4;border-radius:3px}
.fbox{border:1px solid #ccc;border-radius:6px;background:#fff;font-size:8px;color:#333;padding:7px 12px}
.bottom{left:0;top:1176px;width:847px;height:24px;background:#2b2b2b;color:#ddd;font:8.5px/24px "Arimo",sans-serif;text-align:center}
</style>
</head>
<body>
<header class="abs header"></header>
<div class="abs brand">Brindle<br>Marketing</div>
<nav class="abs nav">
  <a class="active" href="#" style="width:74px"><svg width="20" height="18" viewBox="0 0 20 18"><path d="M10 1 1 9h3v8h4v-5h4v5h4V9h3z" fill="#fff"/></svg>Home</a>
  <a href="#" style="width:82px"><svg width="20" height="20" viewBox="0 0 20 20"><circle cx="10" cy="10" r="6" fill="none" stroke="#fff" stroke-width="4" stroke-dasharray="3 2"/><circle cx="10" cy="10" r="3" fill="#fff"/></svg>Services</a>
  <a href="#" style="width:85px"><svg width="22" height="20" viewBox="0 0 22 20"><circle cx="9" cy="6" r="4.5" fill="#fff"/><path d="M1 19c0-6 4-8 8-8s8 2 8 8z" fill="#fff"/><circle cx="17" cy="13" r="3.5" fill="#fff"/></svg>About Us</a>
  <a href="#" style="width:73px"><svg width="20" height="20" viewBox="0 0 20 20"><circle cx="4" cy="16" r="2.5" fill="#fff"/><path d="M2 9a9 9 0 0 1 9 9M2 3a15 15 0 0 1 15 15" fill="none" stroke="#fff" stroke-width="2.5"/></svg>Blog</a>
  <a href="#" style="width:140px"><svg width="22" height="22" viewBox="0 0 22 22"><circle cx="11" cy="11" r="9.5" fill="none" stroke="#fff" stroke-width="1.8"/><path d="M8 6c-1 3 1 8 5 10l2-2-2-2-1 1c-1-1-2-3-2-4l1-1-2-2z" fill="#fff"/></svg>Contact Us</a>
</nav>

<section class="abs hero"></section>
<div class="abs follow">Follow us on <i></i><i></i><i></i><i></i></div>
<h1 class="abs hero-title">We Grow Your Business</h1>
<div class="abs hero-sub">Searchly Certified Sydney Consultant, Guarantees 25% Increase in Your Searchly Advertising Returns.</div>
<div class="abs hero-text">Let's face it, Online Advertising is expensive and confusing. All companies large and small require the services of a highly qualified Online Marketing Manager, not just another salesman. You need someone who understands...</div>
<div class="abs learn">Learn More<span class="btn-arrow"></span></div>
<div class="abs slider"><div class="slide" role="img" aria-label="Search engine optimisation word collage with a red crosshair"></div></div>
<span class="abs arrow prev"></span><span class="abs arrow next"></span>

<div class="abs optin-bar"></div>
<div class="abs optin-title">Subscribe Newsletter</div>
<div class="abs field" style="left:302px;top:373px;width:121px;height:24px">Enter Your Name</div>
<div class="abs field" style="left:444px;top:373px;width:121px;height:24px">Enter Your Email</div>
<div class="abs dark-btn" style="left:611px;top:374px;width:89px;height:21px">Submit Now<span class="btn-arrow" style="width:13px;height:13px;top:4px;right:4px"></span></div>

<h2 class="abs section">What We Do</h2>
<div class="abs rule"></div>
<div class="abs feature-img" role="img" aria-label="Illustration of a group of people around the world"></div>
<div class="abs about-text">
<p>Lorem ipsum dolor sit amet, consectetuer adipiscing elit. Nam cursus. Morbi ut mi. Nullam enim leo, egestas id, condimentum at, laoreet mattis, massa. Sed eleifend nonummy diam. Praesent mauris ante, elementum et, bibendum at, posuere sit amet, nibh. Duis tincidunt lectus quis dui viverra vestibulum. Suspendisse vulputate aliquam dui. Nulla elementum dui ut augue. Aliquam vehicula mi at mauris. Maecenas placerat, nisl at conse-quat rhoncus, sem nunc gravida justo, quis eleifend arcu velit quis lacus.</p>
<p>Pellentesque habitant morbi tristique senectus et netus et malesuada fames ac turpis egestas. In posuere felis nec tortor. Pellentesque faucibus. Ut accumsan ultricies elit...</p>
</div>

<aside class="abs side">
  <h3>Subscribe Newsletter</h3>
  <p>Lorem ipsum dolor sit amet, consectetuer adipiscing elit. Nam</p>
  <div class="abs field" style="left:9px;top:69px;width:174px;height:22px;background:#f4f4f4">Username :</div>
  <div class="abs field" style="left:9px;top:102px;width:174px;height:22px;background:#f4f4f4">Emaul Adress :</div>
  <div class="abs blue-btn" style="left:124px;top:142px;width:56px;height:18px">Submit</div>
</aside>

<div class="abs card" style="left:77px;top:652px"><h4>Web Design</h4><div class="icon" role="img" aria-label="Brushes in a glass icon" style="background:linear-gradient(#fff,#cfcfcf)"></div><p>We focus on getting you the best return for your advertising dollar, while you focus on running your business.</p></div>
<div class="abs card" style="left:324px;top:652px"><h4>Social Media Management</h4><div class="icon" role="img" aria-label="Connected people icon" style="background:linear-gradient(#fff,#d5d5d5)"></div><p>We focus on getting you the best return for your advertising dollar, while you focus on running your business.</p></div>
<div class="abs card" style="left:561px;top:652px"><h4>Mobile Apps</h4><div class="icon" role="img" aria-label="Smartphone with app icons" style="background:linear-gradient(#fff,#cfcfcf)"></div><p>We focus on getting you the best return for your advertising dollar, while you focus on running your business.</p></div>
<div class="abs card" style="left:77px;top:795px"><h4>SEO/PPC Traffic</h4><div class="icon" role="img" aria-label="Search optimisation icon" style="background:linear-gradient(#fff,#d0dbe8)"></div><p>We focus on getting you the best return for your advertising dollar, while you focus on running your business.</p></div>
<div class="abs card" style="left:324px;top:795px"><h4>Display</h4><div class="icon" role="img" aria-label="Computer monitor icon" style="background:linear-gradient(#fff,#bcdff3)"></div><p>We focus on getting you the best return for your advertising dollar, while you focus on running your business.</p></div>
<div class="abs card" style="left:561px;top:795px"><h4>On &amp; Offline Marketing</h4><div class="icon" role="img" aria-label="Marketing arrows icon" style="background:linear-gradient(#fff,#cde3f3)"></div><p>We focus on getting you the best return for your advertising dollar, while you focus on running your business.</p></div>

<div class="abs partners"><span>Searchly</span><span>Clipvale</span><span>Chirpline</span><span>Reelnest</span><span>Friendhall</span><span>Dealgrove</span><span>Findwell</span><span>Yodelix</span><span>Worknet</span><span>Pagesmith</span><span>Cartloom</span></div>

<div class="abs foot-rule"></div>
<div class="abs col-title" style="left:88px;top:1012px">FOLLOW US</div>
<div class="abs social" style="left:90px;top:1045px"><i></i>Friendhall</div>
<div class="abs social" style="left:90px;top:1088px"><i style="border-radius:50%"></i>Chirpline</div>
<div class="abs social" style="left:90px;top:1130px;color:#222"><i style="background:#2a7ab8"></i>Worknet</div>
<div class="abs vsep" style="left:210px"></div>
<div class="abs col-title" style="left:229px;top:1017px">Help Me Choose</div>
<ul class="abs flink" style="left:231px;top:1042px"><li>Benefits of LedgerLeaf</li><li>Best Accounts Software for Me?</li><li>Compare LedgerLeaf Online Products</li><li>Compare LedgerLeaf Desktop Products</li><li>How-to videos - Desktop Products</li><li>Customer Testimonials</li></ul>
<div class="abs vsep" style="left:420px"></div>
<div class="abs col-title" style="left:437px;top:1017px">Search Marketing</div>
<ul class="abs flink" style="left:435px;top:1040px"><li>Search Engine Optisation</li><li>Pay-per-click Advertising</li><li>Mobile Search Marketing</li><li>Search Engine Optisation</li><li>Pay-per-click Advertising</li><li>Mobile Search Marketing</li></ul>
<div class="abs vsep" style="left:581px"></div>
<div class="abs col-title" style="left:600px;top:1012px">Contact Now</div>
<div class="abs fbox" style="left:600px;top:1042px;width:147px;height:24px">----Name----</div>
<div class="abs fbox" style="left:600px;top:1072px;width:147px;height:24px">----Email----</div>
<div class="abs fbox" style="left:600px;top:1102px;width:147px;height:46px">---- Your Message ------</div>
<div class="abs blue-btn" style="left:690px;top:1152px;width:55px;height:18px">Submit</div>

<footer class="abs bottom">Copyright © 2013 Brindle Marketing, LLC. All rights reserved.</footer>
</body>
</html>
```